Harbourline Advisory Group Wordpress Design

See attached brief. If you have questions beyond this please let me know. Brief document is HA Group Website Design v1. Other documents are files from logo creation and business cards to give you an idea of colours and images. Also see document that shows examples of the types of images I want to display on the website.

Focus of site is for customers and to drive traffic from social media etc. Company is startup consulting business in Customer Experience and Contact Centre. We offer benchmarking, strategy reviews, technology audits. etc

Looking for the site to use the existing Wordpress theme on Nestora or something compatible. Happy to change if there is a good reason for doing so.

Has to be easy to manage ongoing if possible.

Target Market(s)

HAG is a consulting organisation in contact centre and customer experience

Number of Pages Required

4 page

Font styles to use
Serif
Sans Serif

Colors
0255a3
3276b5
33a6d7
0293ce
ffffff
fefdec

Requirements
Must have
• Hosted on Nestora so must be compatible. Preference is to use the theme that is already there (Lumeo) unless there is a reason not to
Nice to have
• see brief

```html
<!DOCTYPE html>
<html lang="en">
<head>
<meta charset="utf-8">
<title>Harbourline Advisory Group</title>
<link href="https://fonts.googleapis.com/css2?family=Ubuntu:wght@300;400;500;700&display=swap" rel="stylesheet">
<style>
:root{
  --navy:#0255a3;
  --mid:#3276b5;
  --sky:#33a6d7;
  --cyan:#0293ce;
  --white:#ffffff;
  --cream:#fefdec;
  --ink:#333a44;
  --muted:#6b7380;
  --line:#e3e6ea;
}
*{box-sizing:border-box;margin:0;padding:0}
html,body{width:1200px;height:3109px;overflow:hidden}
body{font-family:'Ubuntu',sans-serif;color:var(--ink);background:var(--white);position:relative}
section,header,footer{position:relative;width:1200px}
.brand{display:flex;align-items:center;gap:10px;color:var(--navy);font-weight:700;font-size:17px;line-height:1.1}
.brand-dot{width:26px;height:26px;border-radius:50%;background:var(--sky);flex:none}
.site-header{height:92px;display:flex;align-items:center;justify-content:space-between;padding:0 112px}
.main-nav{display:flex;gap:0;height:92px}
.main-nav a{font-size:14px;color:#222;text-decoration:none;display:flex;align-items:center;padding:0 17px;position:relative}
.main-nav a.active{color:var(--mid)}
.main-nav a.active::after{content:"";position:absolute;left:0;right:0;bottom:0;height:5px;background:var(--sky)}
.hero{height:497px;background:linear-gradient(120deg,#c9cdd2 0%,#e9e7e3 35%,#b7bcc3 65%,#d8d6d2 100%)}
.hero-title{position:absolute;left:112px;top:340px;background:var(--navy);color:#fff;font-size:39px;padding:4px 14px;line-height:46px}
.hero-sub{position:absolute;left:112px;top:402px;background:var(--cyan);color:#fff;font-size:19px;padding:0 14px;line-height:38px}
.hero-dots{position:absolute;left:566px;top:535px;display:flex;gap:8px}
.hero-dots span{width:11px;height:11px;border-radius:50%;background:#fff}
.hero-dots span.on{background:var(--navy)}
.welcome{height:210px;text-align:center;padding-top:42px}
.section-title{color:var(--navy);font-size:27px;font-weight:400}
.welcome p{font-size:15px;line-height:22px;color:#555;width:970px;margin:22px auto 0}
.solutions{height:700px;text-align:center;padding-top:36px}
.card-grid{display:grid;grid-template-columns:repeat(3,309px);gap:31px 25px;justify-content:center;margin-top:40px}
.card{height:232px;border:1px solid var(--line);border-radius:3px;padding:17px 26px 0;box-shadow:0 1px 4px rgba(0,0,0,.05)}
.card .icon{width:66px;height:66px;border-radius:50%;background:var(--cyan);margin:0 auto;display:flex;align-items:center;justify-content:center}
.card h3{font-size:14px;font-weight:400;color:#222;margin:18px 0 16px;line-height:19px}
.card p{font-size:12px;line-height:20px;color:#777}
.card.featured{background:var(--navy);border-color:var(--navy);padding-top:46px}
.card.featured h3{color:#fff;font-weight:500;margin-top:0}
.card.featured p{color:#dce8f5}
.card .btn{display:inline-block;margin-top:12px;background:#fff;color:var(--navy);font-size:13px;font-weight:500;padding:8px 26px;border-radius:4px}
.operation{height:460px;background:var(--cream)}
.op-brand{position:absolute;left:112px;top:1596px}
.op-title{position:absolute;left:112px;top:1678px;color:var(--navy);font-size:29px;line-height:32px;font-weight:400}
.op-chart{position:absolute;left:0;top:0}
.why{height:460px;background:linear-gradient(180deg,#1c57a8 0%,#0c4aa0 60%,#0b45a0 100%);color:#fff;text-align:center;padding-top:128px}
.why h2{font-size:31px;font-weight:400}
.why .lead{font-size:15px;font-weight:500;margin-top:18px}
.why p.body{font-size:14px;line-height:21px;width:960px;margin:14px auto 0}
.why .btn{display:inline-block;margin-top:28px;background:var(--cyan);color:#fff;font-size:14px;font-weight:500;padding:7px 26px;border-radius:3px}
.questions{height:330px;text-align:center;padding-top:66px}
.questions h2{font-size:31px;font-weight:400;color:#222}
.quote-grid{display:grid;grid-template-columns:repeat(3,309px);gap:25px;justify-content:center;margin-top:32px}
.quote{height:150px;background:var(--cyan);color:#fff;font-size:16px;line-height:22px;padding:36px 24px 0;text-align:left}
.newsletter{height:91px;background:var(--navy);display:flex;align-items:center;padding:0 114px;color:#fff}
.newsletter span{font-size:15px;width:249px}
.newsletter .field{width:605px;height:29px;background:#0a3f7c;color:#9fb6d3;font-size:12px;line-height:29px;padding-left:12px}
.newsletter .btn{margin-left:19px;width:103px;height:29px;background:var(--cyan);font-size:14px;font-weight:500;line-height:29px;text-align:center}
.site-footer{height:197px}
.foot-brand{position:absolute;left:112px;top:78px}
.foot-col{position:absolute;top:50px;font-size:12px;line-height:20.7px;color:#333;list-style:none}
.legal{height:72px;border-top:1px solid var(--line);display:flex;align-items:center;justify-content:space-between;padding:0 112px 0 110px;font-size:11px;color:#333}
.social{display:flex;gap:5px}
.social span{width:28px;height:28px;border-radius:50%;border:2px solid var(--mid)}
</style>
</head>
<body>
<header class="site-header">
  <div class="brand"><span class="brand-dot"></span><span>Harbourline Advisory<br>Group</span></div>
  <nav class="main-nav">
    <a class="active">Home Page</a><a>Services</a><a>Partners</a><a>Blog</a><a>Get in Touch</a>
  </nav>
</header>

<section class="hero" role="img" aria-label="Photo of a team of consultants collaborating around a table">
  <div class="hero-title">Startup consulting business in</div>
  <div class="hero-sub">Customer Experience and Contact Centre</div>
  <div class="hero-dots"><span class="on"></span><span></span><span></span><span></span></div>
</section>

<section class="welcome">
  <h2 class="section-title">Welcome to Harbourline Advisory Group</h2>
  <p>Harbourline Advisory Group (HA Group) is a consulting company focused on Customer Experience and Contact Centre Solutions. We are small (a few people) but we bring teams together for projects that have expertise in what is required</p>
</section>

<section class="solutions">
  <h2 class="section-title">Our Solutions</h2>
  <div class="card-grid">
    <div class="card"><div class="icon"><svg width="26" height="26" viewBox="0 0 24 24"><path fill="#fff" d="M12 2l3 6.5 7 .8-5.2 4.8 1.5 7L12 17.5 5.7 21l1.5-7L2 9.3l7-.8z"/></svg></div><h3>Strategic Operational Review</h3><p>Lorem Ipsum is simply dummy text of the printing and typesetting industry. Lorem Ipsum has been the industry's standard dummy text ever</p></div>
    <div class="card featured"><h3>Contact Centre Benchmarking</h3><p>Lorem Ipsum is simply dummy text of the printing and typesetting industry. Lorem Ipsum has been the industry's standard dummy text ever</p><span class="btn">Learn More</span></div>
    <div class="card"><div class="icon"><svg width="28" height="24" viewBox="0 0 28 24"><rect x="5" y="4" width="18" height="12" rx="1" fill="none" stroke="#fff" stroke-width="2.2"/><rect x="2" y="18" width="24" height="2.5" rx="1" fill="#fff"/></svg></div><h3>Current State v Future State<br>Technology Analysis</h3><p>Lorem Ipsum is simply dummy text of the printing and typesetting industry. Lorem Ipsum has been the industry's standard dummy text ever</p></div>
    <div class="card"><div class="icon"><svg width="30" height="22" viewBox="0 0 30 22"><path fill="#fff" d="M8 20a6 6 0 010-12 8 8 0 0115-1 6.5 6.5 0 010 13z"/></svg></div><h3>Cloud Readiness Assessment</h3><p>Lorem Ipsum is simply dummy text of the printing and typesetting industry. Lorem Ipsum has been the industry's standard dummy text ever</p></div>
    <div class="card"><div class="icon"><svg width="28" height="24" viewBox="0 0 28 24"><path d="M3 2v19h23" fill="none" stroke="#fff" stroke-width="2.2"/><path d="M6 17l6-7 4 4 8-9" fill="none" stroke="#fff" stroke-width="2.4"/></svg></div><h3>Caller Intent Analysis</h3><p>Lorem Ipsum is simply dummy text of the printing and typesetting industry. Lorem Ipsum has been the industry's standard dummy text ever</p></div>
    <div class="card"><div class="icon"><svg width="26" height="26" viewBox="0 0 24 24"><path fill="#fff" d="M4 7h5a2.5 2.5 0 115 0h4v5a2.5 2.5 0 110 5v4h-5a2.5 2.5 0 10-5 0H4v-5a2.5 2.5 0 100-5z"/></svg></div><h3>Self Service Strategy Review</h3><p>Lorem Ipsum is simply dummy text of the printing and typesetting industry. Lorem Ipsum has been the industry's standard dummy text ever</p></div>
  </div>
</section>

<section class="operation">
  <div class="brand" style="position:absolute;left:112px;top:97px"><span class="brand-dot"></span><span>Harbourline Advisory<br>Group</span></div>
  <h2 class="op-title" style="top:179px">Contact Centre<br>Operation</h2>
  <svg class="op-chart" width="1200" height="460" viewBox="0 0 1200 460" font-family="Ubuntu, sans-serif">
    <defs>
      <linearGradient id="bar" x1="0" y1="0" x2="0" y2="1"><stop offset="0" stop-color="#33a6d7"/><stop offset="1" stop-color="#1470b4"/></linearGradient>
      <linearGradient id="barDark" x1="0" y1="0" x2="0" y2="1"><stop offset="0" stop-color="#3276b5"/><stop offset="1" stop-color="#0b3f80"/></linearGradient>
      <linearGradient id="barLight" x1="0" y1="0" x2="0" y2="1"><stop offset="0" stop-color="#a9cbe4"/><stop offset="1" stop-color="#6a9cc8"/></linearGradient>
    </defs>
    <g stroke="#444" stroke-width="1">
      <line x1="562" y1="58" x2="562" y2="367"/><line x1="622" y1="58" x2="622" y2="367"/><line x1="682" y1="58" x2="682" y2="367"/><line x1="742" y1="58" x2="742" y2="367"/><line x1="802" y1="58" x2="802" y2="367"/><line x1="862" y1="58" x2="862" y2="367"/><line x1="922" y1="58" x2="922" y2="367"/><line x1="982" y1="58" x2="982" y2="367"/><line x1="1042" y1="58" x2="1042" y2="367"/>
      <line x1="562" y1="367" x2="1090" y2="367"/>
    </g>
    <g font-size="13" fill="#222">
      <text x="363" y="91">Knowledge Management</text>
      <text x="363" y="131">Quality Management</text>
      <text x="363" y="172">Work and queue management</text>
      <text x="363" y="212">Workforce Management</text>
      <text x="363" y="253">Performance Management</text>
      <text x="363" y="293">Training and Induction</text>
      <text x="363" y="334">Recruitment</text>
    </g>
    <rect x="562" y="77" width="283" height="20" fill="url(#bar)"/>
    <rect x="562" y="117" width="108" height="20" fill="url(#bar)"/>
    <rect x="562" y="158" width="349" height="20" fill="url(#barLight)"/>
    <rect x="562" y="198" width="186" height="20" fill="url(#barDark)"/>
    <rect x="562" y="239" width="198" height="20" fill="url(#barDark)"/>
    <rect x="562" y="279" width="192" height="20" fill="url(#bar)"/>
    <rect x="562" y="320" width="403" height="20" fill="url(#barDark)"/>
    <g font-size="11" fill="#fff" text-anchor="end">
      <text x="840" y="91">47%</text><text x="665" y="131">18%</text><text x="906" y="172">58%</text><text x="743" y="212">31%</text><text x="755" y="253">33%</text><text x="749" y="293">32%</text><text x="960" y="334">67%</text>
    </g>
    <g font-size="14" fill="#222" text-anchor="middle">
      <text x="565" y="394">0%</text><text x="635" y="394">10%</text><text x="690" y="394">20%</text><text x="749" y="394">30%</text><text x="806" y="394">40%</text><text x="865" y="394">50%</text><text x="923" y="394">60%</text><text x="982" y="394">70%</text><text x="1042" y="394">80%</text>
    </g>
  </svg>
</section>

<section class="why" role="img" aria-label="Blue-tinted photo of busy commuters walking through a concourse">
  <h2>Why Organisation Use Us</h2>
  <div class="lead">NO Bullshit Consulting, pragmatic advice, straight forward answers</div>
  <p class="body">We are technology experts, but not technology geeks. We don't care that it's cool technology, we care about the changes it can make to Customer Experience and to your bottom line. We not only know who does what in the market, we know how good they are, how good their last projects were and who their channel is and how good their channel is. We spend our time knowing this stuff so you don't have to. We are operationally focused, all of our consultants have spent time in delivery roles within the contact centre front line. We understand the business, not just the technology.</p>
  <span class="btn">Read More</span>
</section>

<section class="questions">
  <h2>Customers Questions</h2>
  <div class="quote-grid">
    <div class="quote">"Do you feel like you are paying for a Veloce of contact centre solutions but driving it like a Commuto, but without the economy?"</div>
    <div class="quote">"Are you confused about which contact centre solution might be the right one for you?"</div>
    <div class="quote">"Are you letting your service provider or vendor drive your technology or contact centre decisions"</div>
  </div>
</section>

<section class="newsletter">
  <span>Sign Up To Our Monthly Newsletter</span>
  <div class="field">Enter Your Email Address</div>
  <div class="btn">Subscribe</div>
</section>

<footer class="site-footer">
  <div class="brand foot-brand"><span class="brand-dot"></span><span>Harbourline Advisory<br>Group</span></div>
  <ul class="foot-col" style="left:466px"><li>Home Page</li><li>Services</li><li>Partners</li><li>Blog</li><li>Get in Touch</li></ul>
  <ul class="foot-col" style="left:657px"><li>Privacy Policy</li><li>Terms &amp; Conditions</li><li>Legal Notice</li></ul>
  <ul class="foot-col" style="left:862px"><li>Harbourline Office</li><li>Quayside Lane 24b</li><li>20457 Hamburg</li><li>Germany</li><li>Telephone: +49 40 5550 1234</li><li>E-mail: hello@harbourline.example</li></ul>
</footer>
<div class="legal">
  <span>© 2015 Company Name ,All Rights Reserved</span>
  <div class="social" style="margin-right:-16px"><span></span><span></span></div>
  <span style="width:40px"></span>
</div>
</body>
</html>
```